Experienced and Professional Marriage Celebrant

I need a web design for my services as a marriage celebrant in the Sydney area. I want people to have the impression I am a modern and professional marriage celebrant who can tailor a wedding ceremony and execute the ceremony with a high level of care and accommodate and adapt to any style of wedding and personalities of couples. I like a mint and pink and black theme and I am not sure whether to use the professional photos of me, might be too stiff! But would like to see ideas you can come up with. Happy to use other photos you might have

Reason: I have haven't been able to respond as quickly as I would have liked this last week to comments so extending a few days. Thanks

```html
<!DOCTYPE html>
<html lang="en">
<head>
<meta charset="utf-8">
<title>Lena Marlowe Celebrant</title>
<link rel="stylesheet" href="https://fonts.googleapis.com/css2?family=Quicksand:wght@300;400;500;600&display=swap">
<style>
  :root {
    --header-bg: #323232;
    --nav-text: #f2f2f2;
    --band-pink: #c98ccb;
    --band-text: #ffffff;
    --page-bg: #ffffff;
    --ink: #3d3d3d;
    --ink-soft: #555555;
    --rule: #d6d6d6;
    --mint: #c9efdc;
    --mint-quote: #6f7f78;
    --mint-ink: #4a5a54;
    --footer-bg: #141414;
    --footer-text: #d8d8d8;
    --footer-rule: #3a3a3a;
    --bottom-bg: #2d2d2d;
    --bottom-text: #b9b9b9;
    --button-border: #8a8a8a;
  }
  * { box-sizing: border-box; margin: 0; padding: 0; }
  html, body { width: 935px; height: 1200px; overflow: hidden; }
  body {
    position: relative;
    background: var(--page-bg);
    font-family: "Quicksand", sans-serif;
    color: var(--ink);
  }
  .abs { position: absolute; }

  /* Header */
  .site-header { left: 0; top: 0; width: 935px; height: 45px; background: var(--header-bg); }
  .brand { left: 85px; top: 9px; font-size: 22px; font-weight: 400; color: #ffffff; letter-spacing: .3px; }
  .main-nav { right: 85px; top: 16px; display: flex; gap: 22px; }
  .main-nav a { color: var(--nav-text); text-decoration: none; font-size: 11.5px; font-weight: 500; letter-spacing: 1px; }

  /* Hero */
  .hero { left: 0; top: 45px; width: 935px; height: 345px;
    background: linear-gradient(180deg, #a9c3d3 0%, #8ea5a4 30%, #4d5a3a 55%, #8a7462 75%, #b69478 100%); }
  .tagline-band { left: 0; top: 390px; width: 935px; height: 46px; background: var(--band-pink); }
  .tagline { left: 83px; top: 16px; font-size: 13.5px; letter-spacing: 1.4px; color: var(--band-text); font-weight: 500; }

  /* Main */
  .page-title { left: 83px; top: 458px; font-size: 24px; font-weight: 300; letter-spacing: 1.6px; color: var(--ink); }
  .rule { height: 1px; background: var(--rule); }
  .section-title { font-size: 13.5px; font-weight: 500; letter-spacing: 1.3px; text-transform: uppercase; color: var(--ink); }
  .body-copy { font-size: 11.3px; line-height: 16.6px; letter-spacing: .6px; color: var(--ink-soft); font-weight: 500; }
  .button { display: flex; align-items: center; justify-content: center; gap: 6px;
    border: 1px solid var(--button-border); font-size: 9px; font-weight: 700; letter-spacing: 1.2px;
    color: var(--ink); text-transform: uppercase; height: 21px; }

  .video-thumb { left: 83px; top: 532px; width: 245px; height: 161px;
    background: linear-gradient(135deg, #a9bfd6 0%, #c7d3df 40%, #8a8f9c 70%, #3f4350 100%); }
  .play-mark { left: 83px; top: 532px; }

  .column-divider { left: 602px; top: 458px; width: 1px; height: 475px; background: var(--rule); }
  .featured-image { left: 623px; top: 481px; width: 219px; height: 132px;
    background: radial-gradient(ellipse at 40% 45%, #f39a7a 0%, #e26f55 35%, #a54a33 65%, #4a2d23 100%); }

  .testimonial { left: 630px; top: 732px; width: 210px; height: 171px; background: var(--mint); border-radius: 10px; }
  .testimonial-tail { left: 646px; top: 900px; }
  .quote-mark { left: 641px; top: 732px; font-size: 50px; font-weight: 700; color: var(--mint-quote); line-height: 1; font-family: Georgia, serif; }
  .testimonial-text { left: 645px; top: 741px; width: 184px; font-size: 11.3px; line-height: 15.4px; letter-spacing: .5px; color: var(--mint-ink); font-weight: 500; text-indent: 32px; }
  .testimonial-author { right: 116px; top: 880px; font-size: 11px; letter-spacing: .6px; color: #7e9a8e; font-weight: 500; }

  /* Footer */
  .site-footer { left: 0; top: 957px; width: 935px; height: 201px; background: var(--footer-bg); }
  .portrait { left: 81px; top: 982px; width: 112px; height: 140px;
    background: linear-gradient(180deg, #3b3b3b 0%, #6e5a4c 40%, #b88fc2 80%, #2a2a2a 100%); }
  .footer-title { font-size: 13.5px; font-weight: 500; letter-spacing: 1.4px; color: #ffffff; text-transform: uppercase; }
  .footer-copy { font-size: 11.3px; line-height: 16.6px; letter-spacing: .7px; color: var(--footer-text); font-weight: 500; }
  .footer-divider { width: 1px; height: 130px; background: var(--footer-rule); top: 992px; }
  .sitemap-list { list-style: none; }
  .sitemap-list li { font-size: 11.3px; line-height: 16.8px; letter-spacing: .8px; color: var(--footer-text); font-weight: 500; }
  .connect-list { list-style: none; }
  .connect-list li { display: flex; align-items: center; gap: 5px; font-size: 11.3px; letter-spacing: .8px; color: var(--footer-text); font-weight: 500; height: 21px; }
  .connect-list .square { width: 13px; height: 13px; background: #8c8c8c; border-radius: 2px; }

  .bottom-bar { left: 0; top: 1158px; width: 935px; height: 42px; background: var(--bottom-bg); }
  .copyright { left: 95px; top: 15px; font-size: 11px; letter-spacing: 1.1px; color: var(--bottom-text); font-weight: 500; }
</style>
</head>
<body>

<header class="abs site-header">
  <div class="abs brand">Lena Marlowe Celebrant</div>
  <nav class="abs main-nav">
    <a href="#">HOME</a>
    <a href="#">ABOUT LENA</a>
    <a href="#">SERVICES</a>
    <a href="#">GALLERY</a>
    <a href="#">CONTACT US</a>
  </nav>
</header>

<div class="abs hero" role="img" aria-label="Wedding party walking hand in hand along a beach at sunset"></div>

<div class="abs tagline-band">
  <p class="abs tagline">CURABITUR VIVERRA, NEQUE MALESUADA RHONCUS, VEHICULA TORTOR NEC...</p>
</div>

<main>
  <h1 class="abs page-title">Welcome to Our Page</h1>
  <div class="abs rule" style="left:83px;top:495px;width:503px;"></div>

  <h2 class="abs section-title" style="left:83px;top:507px;">Curabitur viverra, neque malesuada rhoncus</h2>
  <div class="abs video-thumb" role="img" aria-label="Video still of a celebrant leading a beach wedding ceremony"></div>
  <svg class="abs play-mark" width="245" height="161" viewBox="0 0 245 161" aria-hidden="true">
    <circle cx="122" cy="80" r="22" fill="rgba(0,0,0,.55)"/>
    <polygon points="115,69 115,91 133,80" fill="#ffffff"/>
  </svg>
  <p class="abs body-copy" style="left:343px;top:534px;width:240px;">In hac habitasse platea dictumst. Etiam eu arcu eros. Aenean nulla mi, bibendum lacinia augue vel, auctor laoreet dolor. Nulla lacus magna, tristique sit amet orci a, cursus venenatis magna.</p>
  <a class="abs button" style="left:400px;top:636px;width:116px;">Watch video
    <svg width="10" height="8" viewBox="0 0 10 8" aria-hidden="true"><rect width="10" height="8" rx="1.5" fill="#333"/><polygon points="4,2 4,6 7,4" fill="#fff"/></svg>
  </a>

  <div class="abs rule" style="left:83px;top:712px;width:503px;"></div>
  <h2 class="abs section-title" style="left:83px;top:730px;">Phasellus vitae tortor ac ipsum viverra viverra</h2>
  <p class="abs body-copy" style="left:84px;top:757px;width:495px;">Aliquam sodales pharetra magna eget tincidunt. Sed euismod blandit turpis, ac ultrices augue imperdiet vitae. Aenean feugiat facilisis diam at rutrum. Aenean vestibulum, ipsum id iaculis varius, dui velit vehicula arcu, in rutrum augue nibh nec mi. Etiam hendrerit, orci at condimentum elementum, nibh massa aliquet urna, non dignissim magna libero tempor urna. In gravida leo eget.</p>
  <a class="abs button" style="left:83px;top:860px;width:116px;">Read more</a>

  <div class="abs column-divider"></div>

  <aside>
    <h2 class="abs section-title" style="left:626px;top:461px;">Featured article</h2>
    <div class="abs featured-image" role="img" aria-label="Coral orchid table centrepiece at a wedding reception"></div>
    <p class="abs body-copy" style="left:623px;top:621px;width:228px;">Morbi accumsan massa id elit fringilla vehicula.  In ut dui ante.</p>
    <a class="abs button" style="left:678px;top:658px;width:116px;">Read more</a>

    <div class="abs rule" style="left:623px;top:696px;width:228px;"></div>
    <h2 class="abs section-title" style="left:628px;top:710px;">Testimonials</h2>
    <div class="abs testimonial"></div>
    <svg class="abs testimonial-tail" width="24" height="22" viewBox="0 0 24 22" aria-hidden="true">
      <polygon points="0,0 22,0 22,22" fill="var(--mint)"/>
    </svg>
    <div class="abs quote-mark">&ldquo;</div>
    <p class="abs testimonial-text">Nunc a consequat risus, vitae sagittis lectus. Quisque eu egestas nunc. In ac massa ipsum. Sed id nulla dui. Interdum et malesuada fames ac ante ipsum primis in faucibus. In a elit nec justo scelerisque fringilla a eget libero.</p>
    <p class="abs testimonial-author">— Jane Doe</p>
  </aside>
</main>

<footer class="abs site-footer"></footer>
<div class="abs portrait" role="img" aria-label="Portrait of the celebrant in a lilac shirt"></div>
<h3 class="abs footer-title" style="left:216px;top:988px;">About Lena</h3>
<p class="abs footer-copy" style="left:216px;top:1008px;width:240px;">Aliquam sodales pharetra magna eget tincidunt. Sed euismod blandit turpis, ac ultrices augue imperdiet vitae. Aenean feugiat facilisis diam at rutrum. Aenean vestibulum, dui velit vehicula arcu, in rutrum augue nibh nec mi.</p>
<div class="abs footer-divider" style="left:469px;"></div>
<h3 class="abs footer-title" style="left:492px;top:988px;">Sitemap</h3>
<ul class="abs sitemap-list" style="left:492px;top:1008px;">
  <li>Home</li><li>About Lena</li><li>Services</li><li>Gallery</li><li>Testimonials</li><li>Contact Us</li>
</ul>
<div class="abs footer-divider" style="left:668px;"></div>
<h3 class="abs footer-title" style="left:689px;top:988px;">Connect</h3>
<ul class="abs connect-list" style="left:689px;top:1012px;">
  <li><span class="square"></span>Friendline</li>
  <li><span class="square"></span>Circleplus</li>
  <li><span class="square"></span>Chirpnet</li>
</ul>

<div class="abs bottom-bar">
  <p class="abs copyright">COPYRIGHT © LENA MARLOWE CELEBRANT 2014</p>
</div>

</body>
</html>
```